Dietitian clinic needs a business card design

We need a business card design for a new dietitian group based in Singapore called "Lantern and Tide". We provide expert, personalised nutrition care to support a wide range of health needs, from chronic conditions to mindful eating. Our team also offers consulting, speaking, and tailored solutions for healthcare providers, organisations, and food services.

Target Market(s)

Adults

Industry/Entity Type

Healthcare

Contact Information for Business Card

Name, position, contact number, email, website address, our logo

Requirements
Nice to have
• Clean, professional but welcoming look

```html
<!DOCTYPE html>
<html lang="en">
<head>
<meta charset="utf-8">
<title>Lantern and Tide – Business Card</title>
<link href="https://fonts.googleapis.com/css2?family=Playfair+Display:wght@800&family=Arimo:wght@400&display=swap" rel="stylesheet">
<style>
  :root {
    --teal: #25596b;
    --blush: #e0a3a4;
    --paper: #ffffff;
    --backdrop: #2a2a2a;
    --ink-light: #ffffff;
  }
  * { margin: 0; padding: 0; box-sizing: border-box; }
  html, body { width: 1200px; height: 875px; overflow: hidden; }
  body {
    background: var(--backdrop);
    position: relative;
    font-family: "Arimo", Arial, sans-serif;
  }
  .card {
    position: absolute;
    top: 277px;
    width: 550px;
    height: 320px;
    border-radius: 18px;
    overflow: hidden;
    box-shadow: 0 14px 30px rgba(0,0,0,0.45);
  }
  .card--front { left: 35px; background: var(--teal); }
  .card--back { left: 615px; background: var(--paper); }

  .brand-name {
    font-family: "Playfair Display", Georgia, serif;
    font-weight: 800;
    line-height: 0.9;
    letter-spacing: -0.5px;
  }
  .card--front .brand-name {
    position: absolute;
    left: 0; right: 0; top: 95px;
    text-align: center;
    color: var(--blush);
    font-size: 58px;
  }
  .card--back .brand-name {
    position: absolute;
    left: 345px; width: 190px; top: 95px;
    text-align: center;
    color: var(--teal);
    font-size: 40px;
  }

  .card__wave { position: absolute; inset: 0; }

  .contact {
    position: absolute;
    left: 34px;
    top: 120px;
    color: var(--ink-light);
  }
  .contact__name {
    font-family: "Playfair Display", Georgia, serif;
    font-weight: 800;
    font-size: 27px;
    color: var(--blush);
    line-height: 1;
  }
  .contact__role { font-size: 13px; margin-top: 4px; }
  .contact__list { list-style: none; margin-top: 14px; font-size: 12px; line-height: 1.45; }
  .contact__item { display: flex; align-items: flex-start; gap: 9px; margin-top: 3px; }
  .contact__icon { width: 12px; height: 12px; flex: none; margin-top: 2px; fill: var(--blush); }
</style>
</head>
<body>

  <section class="card card--front">
    <p class="brand-name">lantern<br>&amp; tide</p>
  </section>

  <section class="card card--back">
    <svg class="card__wave" viewBox="0 0 550 320" aria-hidden="true">
      <path d="M0 0 H352 C312 60 332 128 412 168 C482 203 482 262 462 320 H0 Z" fill="var(--blush)"/>
      <path d="M0 0 H340 C300 60 320 130 400 170 C470 205 470 260 450 320 H0 Z" fill="var(--teal)" stroke="var(--paper)" stroke-width="4"/>
    </svg>

    <div class="contact">
      <h1 class="contact__name">Daniel Reyes</h1>
      <p class="contact__role">Founder &amp; CEO</p>
      <ul class="contact__list">
        <li class="contact__item">
          <svg class="contact__icon" viewBox="0 0 12 12"><path d="M6 0a4 4 0 0 0-4 4c0 3 4 8 4 8s4-5 4-8a4 4 0 0 0-4-4zm0 5.5A1.5 1.5 0 1 1 6 2.5a1.5 1.5 0 0 1 0 3z"/></svg>
          <span>Street Address Here, City<br>State, Country, ZIP 123</span>
        </li>
        <li class="contact__item">
          <svg class="contact__icon" viewBox="0 0 12 12"><path d="M2.5 0.5l2 2-1 1.5a7 7 0 0 0 4.5 4.5l1.5-1 2 2-1.5 2C5 11.5 0.5 7 0.5 2z"/></svg>
          <span>(123) 456-7890</span>
        </li>
        <li class="contact__item">
          <svg class="contact__icon" viewBox="0 0 12 12"><path d="M0 2h12v8H0zm1 1v.4l5 3.3 5-3.3V3z"/></svg>
          <span>hello@lanternandtide.sg</span>
        </li>
        <li class="contact__item">
          <svg class="contact__icon" viewBox="0 0 12 12"><circle cx="6" cy="6" r="5.2" fill="none" stroke="var(--blush)" stroke-width="1.4"/><path d="M6 .8v10.4M.8 6h10.4" stroke="var(--blush)" stroke-width="1"/></svg>
          <span>lanternandtide.sg</span>
        </li>
      </ul>
    </div>

    <p class="brand-name">lantern<br>&amp; tide</p>
  </section>

</body>
</html>
```